Halverin Link Group B.cards and Letterhead
B. cards
Professional
First Last
Executive
Amber Crest Tower
Office 5817
P.O.Box 6094
Jeddah 23867
Saudi Arabia
name@hlgnet.com
www.hlgnet.com
I want to print cards on pearl paper
either blank or a nice design or the logo

```html
<!DOCTYPE html>
<html lang="en">
<head>
<meta charset="utf-8">
<title>Halverin Link Group Stationery</title>
<link href="https://fonts.googleapis.com/css2?family=Open+Sans:wght@400;700&display=swap" rel="stylesheet">
<style>
:root{
  --backdrop:#dcc9a8;
  --paper:#ffffff;
  --navy:#0d2a5c;
  --blue:#1f5fa8;
  --sky:#5d93cf;
  --ink:#3a3a3a;
  --muted:#8a8a8a;
  --label:#5b4a33;
  --flap-grey:#8e9096;
}
*{box-sizing:border-box;margin:0;padding:0}
html,body{width:1200px;height:346px;overflow:hidden}
body{background:var(--backdrop);font-family:"Open Sans",Arial,sans-serif;position:relative;color:var(--ink)}
.item{position:absolute;background:var(--paper);box-shadow:0 1px 3px rgba(0,0,0,.25);overflow:hidden}
.wave{position:absolute;left:0;width:100%;display:block}
.wave-top{top:0}
.wave-bottom{bottom:0}
.brand{position:absolute;display:flex;align-items:center;gap:3px;color:var(--blue);font-weight:700;white-space:nowrap}
.brand-mark{background:var(--blue);display:inline-block}
.caption{position:absolute;font-size:5px;letter-spacing:.5px;text-transform:uppercase;color:var(--label);text-align:center}
.contact{position:absolute;font-size:3.2px;line-height:1.35;color:var(--ink)}
.contact strong{color:var(--blue)}

/* business cards */
.card-front{left:12px;top:91px;width:104px;height:56px}
.card-back{left:12px;top:173px;width:104px;height:56px}
.card-front .brand{left:6px;top:5px;font-size:5px}
.card-front .brand-mark{width:6px;height:6px}
.card-front .contact{left:60px;top:15px;font-size:3px;line-height:1.3}
.card-back .brand{left:50%;top:20px;transform:translateX(-50%);font-size:6px}
.card-back .brand-mark{width:7px;height:7px}

/* letterheads */
.letterhead-a{left:132px;top:19px;width:204px;height:298px}
.letterhead-b{left:365px;top:19px;width:204px;height:298px}
.letterhead-a .brand,.letterhead-b .brand{left:12px;top:10px;font-size:7px}
.letterhead-a .brand-mark,.letterhead-b .brand-mark{width:9px;height:9px}
.letterhead-a .contact{left:140px;top:254px}
.letterhead-b .contact{left:12px;top:262px}

/* envelopes */
.envelope-front{left:612px;top:19px;width:247px;height:125px}
.envelope-back{left:612px;top:173px;width:247px;height:110px}
.envelope-front .brand,.envelope-back .brand{left:12px;top:10px;font-size:7px}
.envelope-front .brand-mark,.envelope-back .brand-mark{width:9px;height:9px}
.envelope-front .contact,.envelope-back .contact{left:12px;top:26px}

.envelope-open{left:893px;top:19px;width:235px;height:293px;background:transparent;box-shadow:none;overflow:visible}
.envelope-open svg{position:absolute;left:0;top:0}
</style>
</head>
<body>

<div class="item card-front">
  <div class="brand"><span class="brand-mark"></span>Halverin Link Group</div>
  <svg class="wave wave-top" width="104" height="20" viewBox="0 0 104 20" preserveAspectRatio="none">
    <defs><linearGradient id="gCard" x1="0" x2="1"><stop offset="0" stop-color="#0d2a5c"/><stop offset="1" stop-color="#1f5fa8"/></linearGradient></defs>
    <path d="M50 0H104V14C88 10 70 4 50 0Z" fill="url(#gCard)"/>
  </svg>
  <div class="contact">
    <strong>First Last</strong><br>Executive<br>Amber Crest Tower<br>Office 5817<br>P.O.Box 6094<br>Jeddah 23867<br>Saudi Arabia<br>name@hlgnet.com<br>www.hlgnet.com
  </div>
</div>
<div class="caption" style="left:12px;top:150px;width:104px">business card front</div>

<div class="item card-back">
  <div class="brand"><span class="brand-mark"></span>Halverin Link Group</div>
  <svg class="wave wave-bottom" width="104" height="18" viewBox="0 0 104 18" preserveAspectRatio="none">
    <path d="M0 8C35 2 70 2 104 10V18H0Z" fill="url(#gCard)"/>
  </svg>
</div>
<div class="caption" style="left:12px;top:232px;width:104px">business card back</div>

<div class="item letterhead-a">
  <svg class="wave wave-top" width="204" height="34" viewBox="0 0 204 34" preserveAspectRatio="none">
    <path d="M70 0H204V26C170 16 120 6 70 0Z" fill="url(#gCard)"/>
    <path d="M60 0C110 6 165 18 204 30V26C170 16 120 6 70 0Z" fill="#5d93cf"/>
  </svg>
  <div class="brand"><span class="brand-mark"></span>Halverin Link Group</div>
  <div class="contact">Amber Crest Tower<br>Office 5817<br>P.O.Box 6094<br>Jeddah 23867<br>Saudi Arabia<br>www.hlgnet.com</div>
</div>
<div class="caption" style="left:132px;top:321px;width:204px">letterhead design one</div>

<div class="item letterhead-b">
  <svg class="wave wave-top" width="204" height="34" viewBox="0 0 204 34" preserveAspectRatio="none">
    <path d="M70 0H204V26C170 16 120 6 70 0Z" fill="url(#gCard)"/>
    <path d="M60 0C110 6 165 18 204 30V26C170 16 120 6 70 0Z" fill="#5d93cf"/>
  </svg>
  <div class="brand"><span class="brand-mark"></span>Halverin Link Group</div>
  <div class="contact">Amber Crest Tower, Office 5817, P.O.Box 6094, Jeddah 23867, Saudi Arabia &nbsp; name@hlgnet.com &nbsp; www.hlgnet.com</div>
  <svg class="wave wave-bottom" width="204" height="20" viewBox="0 0 204 20" preserveAspectRatio="none">
    <path d="M0 12C70 2 140 2 204 10V20H0Z" fill="url(#gCard)"/>
  </svg>
</div>
<div class="caption" style="left:365px;top:321px;width:204px">letterhead design two</div>

<div class="item envelope-front">
  <svg class="wave wave-top" width="247" height="30" viewBox="0 0 247 30" preserveAspectRatio="none">
    <path d="M90 0H247V24C200 12 150 4 90 0Z" fill="url(#gCard)"/>
  </svg>
  <div class="brand"><span class="brand-mark"></span>Halverin Link Group</div>
  <div class="contact">Amber Crest Tower<br>Office 5817<br>P.O.Box 6094<br>Jeddah 23867</div>
</div>
<div class="caption" style="left:612px;top:148px;width:247px">envelope front</div>

<div class="item envelope-back">
  <svg class="wave wave-top" width="247" height="30" viewBox="0 0 247 30" preserveAspectRatio="none">
    <path d="M90 0H247V24C200 12 150 4 90 0Z" fill="url(#gCard)"/>
  </svg>
  <div class="brand"><span class="brand-mark"></span>Halverin Link Group</div>
  <div class="contact">Amber Crest Tower<br>Office 5817<br>P.O.Box 6094<br>Jeddah 23867</div>
</div>
<div class="caption" style="left:612px;top:287px;width:247px">envelope back</div>

<div class="item envelope-open">
  <svg width="235" height="293" viewBox="0 0 235 293">
    <defs>
      <linearGradient id="gFlap" x1="0" x2="0" y1="0" y2="1"><stop offset="0" stop-color="#0d2a5c"/><stop offset="1" stop-color="#1f5fa8"/></linearGradient>
      <linearGradient id="gInside" x1="0" x2="0" y1="0" y2="1"><stop offset="0" stop-color="#6e7076"/><stop offset="1" stop-color="#b4b6ba"/></linearGradient>
    </defs>
    <path d="M0 0H235V42C180 30 60 30 0 42Z" fill="url(#gFlap)"/>
    <path d="M0 42C60 30 180 30 235 42V125H0Z" fill="#eef0f3"/>
    <path d="M8 78C60 64 175 64 227 78V120H8Z" fill="url(#gInside)"/>
    <rect x="0" y="150" width="235" height="140" fill="#ffffff"/>
    <path d="M0 150L117 210L235 150" fill="none" stroke="#d6d8dc" stroke-width="1"/>
    <path d="M0 290L100 220M235 290L135 220" stroke="#e2e4e7" stroke-width="1"/>
  </svg>
</div>
<div class="caption" style="left:893px;top:316px;width:235px">envelope with flap</div>

</body>
</html>
```